Morvell Agronomics, Inc. Business Card

We are joint venture hybrid vegetable seed company. We design & breed application specific products for fresh market and processing applications. We are looking for a business card that will have impact and convey elegance, excellence, high technology, and have enormous eye appeal. It needs to be unique in design and can incorporate photos, or symbols as the case may be.

I very much enjoy the minimalist approach to Quorin's product designs. We would like to include a tag line in the business card: Breeding Success

Target Market(s)

We breed proprietary products that provide better solutions for growers, harvesters, packers, shippers, wholesalers, retailers, consumers, and processors. Regional seed distributors worldwide are our primary clients and then growers. We need to appeal first and foremost to the distributors who will be representing us and selling the products in their target markets.

Industry/Entity Type

Business

Requirements
Must have
• It will have a picture of a cluster of tomatoes on one side and the other side will include the logo, a tag line, our contact information, and a possibly a picture or symbol. I want the contact side to be edgy and convey elegance, solidity, and exclusivity.
Nice to have
• Surprise us with something special.
Should not have
• Card needs to work well with the green logo so it can't be diminished by the background color of the card.

```html
<!DOCTYPE html>
<html lang="en">
<head>
<meta charset="utf-8">
<title>Morvell Agronomics, Inc. – Business Card</title>
<link rel="stylesheet" href="https://fonts.googleapis.com/css2?family=Questrial&display=swap">
<style>
  :root {
    --bg: #c9c9c9;
    --green-deep: #0c4f3b;
    --green-mid: #16684c;
    --green-bright: #4fb13c;
    --green-light: #8fd15a;
    --white: #ffffff;
    --tomato-red: #c8241c;
    --leaf-green: #3d6b33;
    --font: "Questrial", "Century Gothic", sans-serif;
  }
  * { box-sizing: border-box; margin: 0; padding: 0; }
  html, body { width: 1200px; height: 900px; overflow: hidden; }
  body {
    background: var(--bg);
    font-family: var(--font);
    display: flex;
    flex-direction: column;
    align-items: center;
    justify-content: center;
    gap: 56px;
  }
  .card {
    position: relative;
    width: 620px;
    height: 354px;
    border-radius: 24px;
    overflow: hidden;
    box-shadow: 0 8px 20px rgba(0,0,0,0.18);
  }
  .card-art { position: absolute; inset: 0; width: 100%; height: 100%; }

  /* Front */
  .brand {
    position: absolute;
    left: 22px;
    top: 112px;
    width: 250px;
    display: flex;
    align-items: center;
    gap: 10px;
    color: var(--green-deep);
    font-size: 23px;
    line-height: 1.15;
  }
  .brand-dot {
    flex: 0 0 auto;
    width: 34px; height: 34px;
    border-radius: 50%;
    background: var(--green-bright);
  }
  .tagline {
    position: absolute;
    top: 300px;
    font-size: 19px;
    letter-spacing: 13px;
  }
  .tagline-first { left: 34px; color: var(--green-deep); }
  .tagline-second { left: 318px; color: var(--white); }

  .contact {
    position: absolute;
    left: 360px;
    top: 44px;
    color: var(--white);
  }
  .contact-name {
    color: var(--green-light);
    font-size: 22px;
    margin-left: 30px;
  }
  .contact-title {
    font-size: 17px;
    margin: 4px 0 0 40px;
  }
  .contact-list { list-style: none; margin-top: 42px; font-size: 19px; }
  .contact-list li { display: flex; align-items: flex-start; gap: 6px; line-height: 1.3; }
  .contact-icon { width: 20px; height: 20px; margin-top: 3px; flex: 0 0 auto; }
  .contact-list .indent { padding-left: 26px; }

  /* Back */
  .brand-back {
    position: absolute;
    right: 26px;
    top: 220px;
    width: 190px;
    display: flex;
    align-items: center;
    gap: 8px;
    color: var(--white);
    font-size: 19px;
    line-height: 1.15;
  }
  .brand-back .brand-dot { width: 28px; height: 28px; background: var(--green-light); }
</style>
</head>
<body>

<section class="card card-front" aria-label="Card front with contact details">
  <svg class="card-art" viewBox="0 0 620 354" preserveAspectRatio="none" aria-hidden="true">
    <defs>
      <linearGradient id="frontGreen" x1="0" y1="0" x2="1" y2="1">
        <stop offset="0" stop-color="var(--green-mid)"/>
        <stop offset="1" stop-color="var(--green-deep)"/>
      </linearGradient>
      <linearGradient id="bandGreen" x1="0" y1="0" x2="0" y2="1">
        <stop offset="0" stop-color="var(--green-light)"/>
        <stop offset="1" stop-color="var(--green-bright)"/>
      </linearGradient>
    </defs>
    <rect width="620" height="354" fill="url(#frontGreen)"/>
    <path d="M0,0 H342 C326,140 296,262 240,354 H0 Z" fill="url(#bandGreen)"/>
    <path d="M0,0 H302 C288,130 270,262 236,354 H0 Z" fill="var(--white)"/>
  </svg>

  <div class="brand">
    <span class="brand-dot"></span>
    <span>Morvell Agronomics, Inc.</span>
  </div>

  <span class="tagline tagline-first">Breeding</span>
  <span class="tagline tagline-second">Success</span>

  <div class="contact">
    <p class="contact-name">Lena Harwick</p>
    <p class="contact-title">Manager</p>
    <ul class="contact-list">
      <li>
        <svg class="contact-icon" viewBox="0 0 20 20" aria-hidden="true"><path d="M5 2 L8 6 L6.5 8 C7.5 10.5 9.5 12.5 12 13.5 L14 12 L18 15 L16 18 C9 18 2 11 2 4 Z" fill="var(--green-light)"/></svg>
        <span>1535 204 718</span>
      </li>
      <li>
        <svg class="contact-icon" viewBox="0 0 20 20" aria-hidden="true"><g fill="none" stroke="var(--green-light)" stroke-width="1.6"><circle cx="10" cy="10" r="8"/><ellipse cx="10" cy="10" rx="3.5" ry="8"/><path d="M2 10 H18 M3.5 5.5 H16.5 M3.5 14.5 H16.5"/></g></svg>
        <span>www.morvellag.com</span>
      </li>
      <li>
        <svg class="contact-icon" viewBox="0 0 20 20" aria-hidden="true"><rect x="2" y="5" width="16" height="11" rx="1" fill="var(--green-light)"/><path d="M2.5 5.5 L10 11 L17.5 5.5" fill="none" stroke="var(--green-deep)" stroke-width="1.5"/></svg>
        <span>info@morvellag.com</span>
      </li>
      <li>
        <svg class="contact-icon" viewBox="0 0 20 20" aria-hidden="true"><path d="M10 2 L19 10 H16 V18 H12 V13 H8 V18 H4 V10 H1 Z" fill="var(--green-light)"/></svg>
        <span>PO Box 2870</span>
      </li>
      <li class="indent"><span>Riverbend Qld 4217</span></li>
    </ul>
  </div>
</section>

<section class="card card-back" aria-label="Card back">
  <svg class="card-art" viewBox="0 0 620 354" preserveAspectRatio="none">
    <defs>
      <linearGradient id="backGreen" x1="0" y1="0" x2="1" y2="1">
        <stop offset="0" stop-color="var(--green-mid)"/>
        <stop offset="1" stop-color="var(--green-deep)"/>
      </linearGradient>
      <linearGradient id="backBand" x1="0" y1="0" x2="0" y2="1">
        <stop offset="0" stop-color="var(--green-light)"/>
        <stop offset="1" stop-color="var(--green-bright)"/>
      </linearGradient>
      <radialGradient id="photoTone" cx="0.45" cy="0.5" r="0.65">
        <stop offset="0" stop-color="var(--tomato-red)"/>
        <stop offset="0.55" stop-color="#a2331f"/>
        <stop offset="1" stop-color="var(--leaf-green)"/>
      </radialGradient>
    </defs>
    <rect width="620" height="354" fill="url(#backGreen)" aria-hidden="true"/>
    <path d="M0,0 H368 C404,110 400,250 320,354 H0 Z" fill="url(#backBand)" aria-hidden="true"/>
    <path role="img" aria-label="Photo of a cluster of ripe red tomatoes on the vine in a greenhouse" d="M0,0 H348 C382,110 376,250 300,354 H0 Z" fill="url(#photoTone)"/>
  </svg>

  <div class="brand-back">
    <span class="brand-dot"></span>
    <span>Morvell Agronomics, Inc.</span>
  </div>
</section>

</body>
</html>
```